LearnWave Futures Alliance Business Card

Create a very cool business card. Logo is attached.

Learnwave Futures Alliance Mission

The purposes for which the corporation is organized are to promote social welfare within the meaning of section 501(c)(4) of the Internal Revenue Code, including but not limited to: (1) developing and advocating for legislation, regulations, and government programs that improve education through the use of technology, online enabled course design, personalize instruction and increased student engagement; (2) promoting digital literacy driven by private, public and philanthropic efforts that utilize technology for student learning; (3) advocate for competency based educational efforts built upon digital tools, devices and content that support learning programs; (4) develop policy positions that ensure that poor, minority status, and disadvantaged students will benefit from innovative technologies which should provide increased instructional opportunities for postsecondary success and career advancement; (5) conducting research and publicizing positions of higher education institutions and elected officials concerning these issues

Info for Card:

Mark Tavelli, Founder
LearnWave Futures Alliance
412 West Harmon Ave, 6th Floor
Pasadena, CA 90417
o (555) 317-2290
f (555) 941-6612
mark@learnwavefutures.org
website: learnwavefutures.org

```html
<!DOCTYPE html>
<html lang="en">
<head>
<meta charset="utf-8">
<title>LearnWave Futures Alliance Business Card</title>
<link rel="stylesheet" href="https://fonts.googleapis.com/css2?family=Crimson+Pro:wght@400;500&display=swap">
<style>
  :root {
    --page-bg: #e9e7e3;
    --card-white: #fbfbfb;
    --brand-blue: #2f5bb3;
    --brand-blue-deep: #234a9c;
    --brand-blue-light: #5f86d2;
    --ink: #1d1d1f;
    --rule-black: #111;
    --watermark: #e6e9f3;
  }
  html, body {
    margin: 0;
    padding: 0;
    width: 1200px;
    height: 818px;
    overflow: hidden;
    background: var(--page-bg);
  }
  .canvas {
    position: relative;
    width: 1200px;
    height: 818px;
  }
  .card {
    position: absolute;
    left: 75px;
    top: 109px;
    width: 1050px;
    height: 600px;
    background: var(--card-white);
    box-shadow: 0 12px 30px rgba(0,0,0,0.18);
    overflow: hidden;
    font-family: "Crimson Pro", "Times New Roman", serif;
    color: var(--ink);
  }
  .watermark-disc {
    position: absolute;
    left: 470px;
    top: 90px;
    width: 280px;
    height: 280px;
    border-radius: 50%;
    background: var(--watermark);
  }
  .identity {
    position: absolute;
    right: 60px;
    top: 52px;
    text-align: right;
  }
  .identity .name {
    font-size: 50px;
    line-height: 1;
    font-weight: 400;
    letter-spacing: 0.5px;
  }
  .identity .role {
    font-size: 28px;
    margin-top: 6px;
  }
  .rule-line {
    position: absolute;
    left: 0;
    right: 0;
    bottom: 104px;
    height: 3px;
    background: var(--rule-black);
  }
  .brand-band {
    position: absolute;
    left: 0;
    right: 0;
    bottom: 0;
    height: 94px;
    background: linear-gradient(180deg, var(--brand-blue-light) 0%, var(--brand-blue) 45%, var(--brand-blue-deep) 100%);
  }
  .brand-name {
    position: absolute;
    left: 44px;
    bottom: 124px;
    display: flex;
    align-items: center;
    gap: 12px;
    color: var(--brand-blue);
    font-size: 26px;
    font-weight: 500;
    line-height: 1.05;
  }
  .brand-name .mark-dot {
    width: 36px;
    height: 36px;
    border-radius: 50%;
    background: var(--brand-blue);
    flex: none;
  }
  .contacts {
    position: absolute;
    right: 40px;
    bottom: 128px;
    display: flex;
    align-items: flex-end;
    gap: 30px;
    font-size: 19px;
    line-height: 1.5;
  }
  .contact-group { flex: none; }
  .contact-row {
    display: flex;
    align-items: center;
    gap: 8px;
    white-space: nowrap;
  }
  .icon {
    width: 16px;
    height: 16px;
    flex: none;
    fill: var(--brand-blue);
  }
  .address .contact-row { align-items: flex-start; }
  .address .icon { margin-top: 6px; }
</style>
</head>
<body>
<div class="canvas">
  <div class="card">
    <div class="watermark-disc"></div>

    <div class="identity">
      <div class="name">Mark Tavelli</div>
      <div class="role">Founder</div>
    </div>

    <div class="brand-name">
      <span class="mark-dot"></span>
      <span>LearnWave<br>Futures Alliance</span>
    </div>

    <div class="contacts">
      <div class="contact-group phones">
        <div class="contact-row">
          <svg class="icon" viewBox="0 0 24 24"><path d="M6.6 10.8a15 15 0 0 0 6.6 6.6l2.2-2.2c.3-.3.7-.4 1-.2 1.1.4 2.3.6 3.6.6.6 0 1 .4 1 1V20c0 .6-.4 1-1 1A17 17 0 0 1 3 4c0-.6.4-1 1-1h3.5c.6 0 1 .4 1 1 0 1.3.2 2.5.6 3.6.1.3 0 .7-.2 1z"/></svg>
          <span>(555) 317-2290</span>
        </div>
        <div class="contact-row">
          <svg class="icon" viewBox="0 0 24 24"><path d="M6 2h10v6H6z M3 9h18v9h-3v4H6v-4H3z M8 15v5h8v-5z"/></svg>
          <span>(555) 941-6612</span>
        </div>
      </div>

      <div class="contact-group online">
        <div class="contact-row">
          <svg class="icon" viewBox="0 0 24 24"><path d="M2 5h20v14H2z M3.5 6.5 12 13l8.5-6.5z" fill-rule="evenodd"/></svg>
          <span>mark@learnwavefutures.org</span>
        </div>
        <div class="contact-row">
          <svg class="icon" viewBox="0 0 24 24"><path d="M12 2a10 10 0 1 0 0 20 10 10 0 0 0 0-20zm0 2c1.2 1.5 2 3.6 2.2 7H9.8c.2-3.4 1-5.5 2.2-7zM4.1 11a8 8 0 0 1 4-6.1c-.8 1.7-1.2 3.8-1.3 6.1zm0 2h2.7c.1 2.3.5 4.4 1.3 6.1a8 8 0 0 1-4-6.1zm5.7 0h4.4c-.2 3.4-1 5.5-2.2 7-1.2-1.5-2-3.6-2.2-7zm6.1-8.1a8 8 0 0 1 4 6.1h-2.7c-.1-2.3-.5-4.4-1.3-6.1zM17.2 13h2.7a8 8 0 0 1-4 6.1c.8-1.7 1.2-3.8 1.3-6.1z"/></svg>
          <span>www.learnwavefutures.org</span>
        </div>
      </div>

      <div class="contact-group address">
        <div class="contact-row">
          <svg class="icon" viewBox="0 0 24 24"><path d="M12 2a7 7 0 0 0-7 7c0 5 7 13 7 13s7-8 7-13a7 7 0 0 0-7-7zm0 9.5a2.5 2.5 0 1 1 0-5 2.5 2.5 0 0 1 0 5z"/></svg>
          <span>412 West Harmon Ave<br>6th Floor Pasadena, CA 90417</span>
        </div>
      </div>
    </div>

    <div class="rule-line"></div>
    <div class="brand-band"></div>
  </div>
</div>
</body>
</html>
```